New emergency medical service needs a marketing flyer for prospective customers

We need a tri fold brochure on an 8.5 X 11 stock for a new emergency medical service in Pennsylvania. We provide basic first aid and now Covid-19 pre screening and temperature monitoring for special events, large gatherings and businesses. Examples of these would be but not limited to: Sporting events, carnivals, festivals, craft shows, warehouses, churches, manufacturing facilities, industrial buildings, large construction sites, multi occupancy officer buildings. The market for this is pretty much untouched and endless. we would like to use gray as the back ground color and obviously our logo. The final design should grab their attention and communicate the importance of having trained and certified professionals at their event or facility. We want to give them that piece of mind they are in good hands with us.

Target Market(s)

primary focus is going to be on businesses with large offices, large buildings or lots of foot traffic in and out of the building

Requirements
Must have
• gray background, pictures, company phone # , company web site, and contact email address. I will provide all that information to the winner to add at the end.
Nice to have
• pictures that covers the whole front cover with logo at top

```html
<!DOCTYPE html>
<html lang="en">
<head>
<meta charset="utf-8">
<title>Ridgeline Medical Services – Brochure Cover</title>
<link rel="stylesheet" href="https://fonts.googleapis.com/css2?family=Open+Sans:wght@400;600;700;800&display=swap">
<style>
  :root {
    --paper: #f6f5f2;
    --teal: #5bb5a9;
    --teal-soft: #b9dcd5;
    --teal-faint: #9fd0c7;
    --stone: #e4e1dc;
    --ink: #1f1f1f;
    --white: #ffffff;
  }
  html, body { margin: 0; padding: 0; overflow: hidden; background: var(--paper); }
  .cover {
    position: relative;
    width: 1200px;
    height: 927px;
    overflow: hidden;
    background: var(--paper);
    font-family: "Open Sans", Arial, sans-serif;
  }
  .artwork { position: absolute; inset: 0; }
  .brand {
    position: absolute;
    left: 814px;
    top: 386px;
    color: var(--ink);
    font-weight: 800;
    display: flex;
    align-items: center;
    gap: 14px;
  }
  .brand-dot {
    width: 62px; height: 62px;
    border-radius: 50%;
    background: var(--ink);
    flex: none;
  }
  .brand-name { line-height: 1; }
  .brand-name .primary { display: block; font-size: 52px; letter-spacing: 1px; }
  .brand-name .secondary { display: block; font-size: 24px; margin-top: 6px; letter-spacing: 0.5px; }
  .tagline {
    position: absolute;
    left: 834px;
    top: 505px;
    margin: 0;
    color: var(--white);
    font-weight: 600;
    font-size: 21px;
    line-height: 28px;
    letter-spacing: 3.4px;
  }
  .headline {
    position: absolute;
    left: 40px;
    top: 742px;
    margin: 0;
    color: var(--teal);
    font-weight: 700;
    font-size: 37px;
    line-height: 44px;
  }
  .contact {
    position: absolute;
    left: 445px;
    top: 774px;
    color: var(--teal);
  }
  .contact h2 { margin: 0 0 14px; font-size: 22px; font-weight: 700; }
  .contact p { margin: 0; font-size: 13.5px; line-height: 18px; letter-spacing: 1.1px; }
</style>
</head>
<body>
<main class="cover">
  <svg class="artwork" width="1200" height="927" viewBox="0 0 1200 927">
    <defs>
      <linearGradient id="facadeTone" x1="0" y1="0" x2="1" y2="1">
        <stop offset="0" stop-color="#f1efeb"/>
        <stop offset="1" stop-color="#dedad4"/>
      </linearGradient>
    </defs>
    <polygon class="facade-photo" role="img" aria-label="Photo of a modern white building facade"
             points="20,927 560,380 760,250 1200,520 1200,927" fill="url(#facadeTone)" opacity="0.7"/>
    <circle class="accent-disc" cx="975" cy="414" r="351" fill="var(--teal-soft)" opacity="0.82"/>
    <circle class="dot-arc" role="img" aria-label="Dotted arc pattern" cx="600" cy="27" r="310"
            fill="none" stroke="var(--teal-faint)" stroke-width="30" opacity="0.6"/>
    <circle class="ring-top" cx="600" cy="27" r="258" fill="none" stroke="var(--teal)" stroke-width="13"/>
    <circle class="dot-arc" role="img" aria-label="Dotted arc pattern" cx="1236" cy="960" r="370"
            fill="none" stroke="var(--teal-faint)" stroke-width="30" opacity="0.6"/>
    <circle class="ring-bottom" cx="1236" cy="960" r="306" fill="none" stroke="var(--teal)" stroke-width="13"/>
    <g class="plus-icon" fill="var(--teal)">
      <rect x="47" y="61" width="57" height="12"/>
      <rect x="69" y="38" width="12" height="57"/>
    </g>
  </svg>

  <div class="brand">
    <span class="brand-dot"></span>
    <div class="brand-name">
      <span class="primary">RIDGELINE</span>
      <span class="secondary">Medical Services</span>
    </div>
  </div>

  <p class="tagline">BASIC EMERGENCY<br>TRAINING SERVICES</p>

  <h1 class="headline">Learn Basic First<br>Aid from the<br>Experts.</h1>

  <section class="contact">
    <h2>Contact us</h2>
    <p>123 Anywhere St., Any City, ST 12345</p>
    <p>+123-456-7890</p>
    <p>hello@company.com</p>
    <p>www.company.com</p>
  </section>
</main>
</body>
</html>
```